Need a Creative 1 Page Website Design

Looking for a personal website. This is the current site and it needs to be updated. https://olivertrask.com/
Reference - greyharbor.video
quillstudios.nyc
Use the same font used in the current site. But we need to have a more creative website
follow this order and video list https://files.vendrastore.com/document/d/7Kp2LmQx9RtWv4YbNc8HsJd3FgZa6EuTqB1oXiMn5Pw/edit?usp=sharing
screenshots https://box.vendrastore.com/drive/folders/9QwErTy7UiOp3AsDfGhJkLz5XcVbN8mKq?usp=sharing
Make a creative personal website with mostly video content.
Target Market(s)
Music
Number of Pages Required
1 page
Look and feel

```html
<!DOCTYPE html>
<html lang="en">
<head>
<meta charset="utf-8">
<title>Oliver Trask — Director</title>
<link href="https://fonts.googleapis.com/css2?family=Gilda+Display&family=Roboto:wght@400;500;700&display=swap" rel="stylesheet">
<style>
  :root{
    --stage:#949494;
    --brand:#f0474e;
    --ink:#ffffff;
    --rule:rgba(255,255,255,.22);
    --serif:"Gilda Display", Georgia, serif;
    --sans:"Roboto", Arial, sans-serif;
  }
  *{box-sizing:border-box;margin:0;padding:0}
  html,body{width:1200px;height:4057px;overflow:hidden}
  body{background:var(--stage);position:relative;font-family:var(--sans);color:var(--ink)}
  ul{list-style:none}
  .sprite{position:absolute;width:0;height:0}

  .screen{position:absolute;background:var(--brand);box-shadow:0 3px 10px rgba(0,0,0,.3)}
  .screen--desktop{left:54px;top:61px;width:842px;height:1297px}
  .screen--mobile{left:937px;top:61px;width:210px;height:3935px}

  .logo{position:absolute;font-family:var(--serif);font-weight:400;white-space:nowrap;line-height:1}
  .tile{position:relative;overflow:hidden}
  .tile .play{position:absolute;left:50%;top:50%;transform:translate(-50%,-50%)}

  /* desktop */
  .screen--desktop .logo{left:23px;top:10px;font-size:44px}
  .main-nav{position:absolute;right:24px;top:27px;display:flex;gap:19px;font-size:9.5px;letter-spacing:.1px}
  .main-nav li{position:relative;padding-bottom:8px}
  .main-nav .is-active::after{content:"";position:absolute;left:-3px;right:-3px;bottom:0;height:1.5px;background:var(--ink)}
  .main-nav .is-active::before{content:"";position:absolute;left:50%;bottom:1px;margin-left:-3px;border:3px solid transparent;border-bottom-color:var(--ink)}
  .screen--desktop .video-grid{position:absolute;left:20px;top:78px;width:802px;display:grid;grid-template-columns:repeat(4,1fr);column-gap:6px;row-gap:9px}
  .screen--desktop .tile{height:210px}
  .btn-more{position:absolute;display:flex;align-items:center;justify-content:center;gap:5px;border:1.5px solid var(--ink);border-radius:30px;font-weight:700;text-transform:uppercase;white-space:nowrap}
  .screen--desktop .btn-more{left:335px;top:988px;width:172px;height:44px;font-size:10px}
  .divider{position:absolute;height:1px;background:var(--rule)}
  .screen--desktop .divider{left:20px;right:20px;top:1076px}
  .site-footer{position:absolute;left:0;right:0;text-align:center}
  .screen--desktop .footer-logo{left:100px;top:1119px;font-size:44px}
  .contact{position:absolute;display:flex;align-items:center;white-space:nowrap}
  .screen--desktop .contact{left:414px;top:1119px;gap:12px;font-size:16.5px}
  .social{display:flex;gap:10px;font-size:11px;font-weight:500}
  .screen--desktop .social{margin-left:26px}
  .footer-nav{font-weight:500;text-transform:uppercase;white-space:nowrap}
  .footer-nav span{margin:0 16px}
  .screen--desktop .footer-nav{position:absolute;left:0;right:0;top:1202px;text-align:center;font-size:14px}
  .legal{position:absolute;left:0;right:0;text-align:center;white-space:nowrap}
  .screen--desktop .legal{top:1239px;font-size:9.5px}

  /* mobile */
  .screen--mobile .logo{left:10px;top:4px;font-size:33px}
  .burger{position:absolute;right:9px;top:13px}
  .screen--mobile .video-grid{position:absolute;left:8px;top:52px;width:194px;display:flex;flex-direction:column;gap:9.5px}
  .screen--mobile .tile{height:211px}
  .screen--mobile .btn-more{left:19px;top:3610px;width:172px;height:44px;font-size:10px}
  .screen--mobile .divider{left:0;right:0;top:3698px}
  .screen--mobile .footer-logo{left:0;right:0;top:3720px;text-align:center;font-size:33px}
  .screen--mobile .contact{left:12px;top:3766px;gap:6px;font-size:12px}
  .screen--mobile .social{position:absolute;left:0;right:0;top:3802px;justify-content:center;font-size:10px}
  .screen--mobile .footer-nav{position:absolute;left:0;right:0;top:3843px;text-align:center;font-size:8.5px;line-height:14px}
  .screen--mobile .footer-nav span{margin:0 8px}
  .screen--mobile .legal{top:3882px;font-size:8px;line-height:14px}

  /* tile fills */
  .v1{background:linear-gradient(160deg,#3a2a22,#15110f)}
  .v2{background:linear-gradient(180deg,#2a3140 0%,#e8476d 70%,#c02a4c)}
  .v3{background:linear-gradient(110deg,#c01010,#2a0606 70%)}
  .v4{background:linear-gradient(180deg,#c9c2b0,#8fa5a0 60%,#5aa3b3)}
  .v5{background:linear-gradient(180deg,#7a5a3a,#1f4a34 60%,#c2305f)}
  .v6{background:linear-gradient(135deg,#2a2420,#5a4a40 60%,#c8c0b8)}
  .v7{background:linear-gradient(180deg,#3f6a4a,#1d2a2a 55%,#111820)}
  .v8{background:linear-gradient(150deg,#0f3a3a,#3a3030 50%,#d08a80)}
  .v9{background:linear-gradient(120deg,#1a2ad0,#3a1a70 55%,#c040a0)}
  .v10{background:linear-gradient(160deg,#5a8aa0,#c8c0b0 60%,#8a7060)}
  .v11{background:linear-gradient(180deg,#b0a8a0,#3a3430 55%,#1a1a1a)}
  .v12{background:linear-gradient(180deg,#0f2a28,#1a2018 60%,#6a5a30)}
  .v13{background:linear-gradient(180deg,#8a1010,#4a0c0c 55%,#c8b8b0)}
  .v14{background:linear-gradient(160deg,#e0d4b8,#c8a880 60%,#a07a58)}
  .v15{background:linear-gradient(180deg,#e8d8e0,#8a7a88 50%,#1a1a24)}
  .v16{background:linear-gradient(170deg,#6a7a4a,#e05a20 55%,#b0a090)}
</style>
</head>
<body>

<svg class="sprite" aria-hidden="true">
  <symbol id="play" viewBox="0 0 40 40">
    <circle cx="20" cy="20" r="18" fill="none" stroke="#fff" stroke-width="2.5"/>
    <path d="M16 12.5v15l12-7.5z" fill="#fff"/>
  </symbol>
  <symbol id="mail" viewBox="0 0 40 40">
    <circle cx="20" cy="20" r="18" fill="none" stroke="#fff" stroke-width="2"/>
    <rect x="11" y="14" width="18" height="12" fill="none" stroke="#fff" stroke-width="1.8"/>
    <path d="M11 14l9 7 9-7" fill="none" stroke="#fff" stroke-width="1.8"/>
  </symbol>
  <symbol id="arrow" viewBox="0 0 10 10">
    <circle cx="5" cy="5" r="5" fill="#fff"/>
    <path d="M4 2.8L6.2 5 4 7.2" fill="none" stroke="#f0474e" stroke-width="1.4"/>
  </symbol>
</svg>

<!-- Desktop -->
<section class="screen screen--desktop">
  <header>
    <div class="logo">Oliver Trask</div>
    <nav>
      <ul class="main-nav">
        <li class="is-active">DIRECTION</li>
        <li>EXECUTIVE PRODUCTION</li>
        <li>COMMISSIONED</li>
        <li>CONTACT</li>
      </ul>
    </nav>
  </header>

  <ul class="video-grid">
    <li class="tile v1" role="img" aria-label="Music video still: artist seated in a dim room"><svg class="play" width="40" height="40"><use href="#play"/></svg></li>
    <li class="tile v2" role="img" aria-label="Music video still: artist in a pink jacket"><svg class="play" width="40" height="40"><use href="#play"/></svg></li>
    <li class="tile v3" role="img" aria-label="Music video still: red lit doorway"><svg class="play" width="40" height="40"><use href="#play"/></svg></li>
    <li class="tile v4" role="img" aria-label="Music video still: beach scene"><svg class="play" width="40" height="40"><use href="#play"/></svg></li>
    <li class="tile v5" role="img" aria-label="Music video still: artist with long locs"><svg class="play" width="40" height="40"><use href="#play"/></svg></li>
    <li class="tile v6" role="img" aria-label="Music video still: tattooed hand close-up"><svg class="play" width="40" height="40"><use href="#play"/></svg></li>
    <li class="tile v7" role="img" aria-label="Music video still: artist outdoors with chain"><svg class="play" width="40" height="40"><use href="#play"/></svg></li>
    <li class="tile v8" role="img" aria-label="Music video still: close-up in teal light"><svg class="play" width="40" height="40"><use href="#play"/></svg></li>
    <li class="tile v9" role="img" aria-label="Music video still: blue and purple lit van"><svg class="play" width="40" height="40"><use href="#play"/></svg></li>
    <li class="tile v10" role="img" aria-label="Music video still: couple outdoors"><svg class="play" width="40" height="40"><use href="#play"/></svg></li>
    <li class="tile v11" role="img" aria-label="Music video still: low-angle close-up"><svg class="play" width="40" height="40"><use href="#play"/></svg></li>
    <li class="tile v12" role="img" aria-label="Music video still: figure standing at night"><svg class="play" width="40" height="40"><use href="#play"/></svg></li>
    <li class="tile v13" role="img" aria-label="Music video still: vintage red car"><svg class="play" width="40" height="40"><use href="#play"/></svg></li>
    <li class="tile v14" role="img" aria-label="Music video still: artist in sunglasses"><svg class="play" width="40" height="40"><use href="#play"/></svg></li>
    <li class="tile v15" role="img" aria-label="Music video still: artist under pale sky"><svg class="play" width="40" height="40"><use href="#play"/></svg></li>
    <li class="tile v16" role="img" aria-label="Music video still: backyard party with balloons"><svg class="play" width="40" height="40"><use href="#play"/></svg></li>
  </ul>

  <a class="btn-more">See more videos <svg width="10" height="10"><use href="#arrow"/></svg></a>
  <div class="divider"></div>

  <footer>
    <div class="logo footer-logo">Oliver Trask</div>
    <div class="contact">
      <svg width="38" height="38"><use href="#mail"/></svg>
      <span>olivertraskmgmt@mailbox.com</span>
      <ul class="social"><li>Linkwell</li><li>Framehouse</li></ul>
    </div>
    <p class="footer-nav">Direction<span>/</span>Executive Production<span>/</span>Commissioned<span>/</span>Contact</p>
    <p class="legal">© 2020 Oliver Trask . All Rights reserved &nbsp;|&nbsp; Privacy &nbsp;|&nbsp; Terms and use</p>
  </footer>
</section>

<!-- Mobile -->
<section class="screen screen--mobile">
  <header>
    <div class="logo">Oliver Trask</div>
    <svg class="burger" width="20" height="16" viewBox="0 0 20 16" aria-label="Menu"><rect y="0" width="20" height="3" fill="#fff"/><rect y="6.5" width="20" height="3" fill="#fff"/><rect y="13" width="20" height="3" fill="#fff"/></svg>
  </header>

  <ul class="video-grid">
    <li class="tile v1" role="img" aria-label="Music video still: artist seated in a dim room"><svg class="play" width="40" height="40"><use href="#play"/></svg></li>
    <li class="tile v2" role="img" aria-label="Music video still: artist in a pink jacket"><svg class="play" width="40" height="40"><use href="#play"/></svg></li>
    <li class="tile v3" role="img" aria-label="Music video still: red lit doorway"><svg class="play" width="40" height="40"><use href="#play"/></svg></li>
    <li class="tile v4" role="img" aria-label="Music video still: beach scene"><svg class="play" width="40" height="40"><use href="#play"/></svg></li>
    <li class="tile v5" role="img" aria-label="Music video still: artist with long locs"><svg class="play" width="40" height="40"><use href="#play"/></svg></li>
    <li class="tile v6" role="img" aria-label="Music video still: tattooed hand close-up"><svg class="play" width="40" height="40"><use href="#play"/></svg></li>
    <li class="tile v7" role="img" aria-label="Music video still: artist outdoors with chain"><svg class="play" width="40" height="40"><use href="#play"/></svg></li>
    <li class="tile v8" role="img" aria-label="Music video still: close-up in teal light"><svg class="play" width="40" height="40"><use href="#play"/></svg></li>
    <li class="tile v9" role="img" aria-label="Music video still: blue and purple lit van"><svg class="play" width="40" height="40"><use href="#play"/></svg></li>
    <li class="tile v10" role="img" aria-label="Music video still: couple outdoors"><svg class="play" width="40" height="40"><use href="#play"/></svg></li>
    <li class="tile v11" role="img" aria-label="Music video still: low-angle close-up"><svg class="play" width="40" height="40"><use href="#play"/></svg></li>
    <li class="tile v12" role="img" aria-label="Music video still: figure standing at night"><svg class="play" width="40" height="40"><use href="#play"/></svg></li>
    <li class="tile v13" role="img" aria-label="Music video still: vintage red car"><svg class="play" width="40" height="40"><use href="#play"/></svg></li>
    <li class="tile v14" role="img" aria-label="Music video still: artist in sunglasses"><svg class="play" width="40" height="40"><use href="#play"/></svg></li>
    <li class="tile v15" role="img" aria-label="Music video still: artist under pale sky"><svg class="play" width="40" height="40"><use href="#play"/></svg></li>
    <li class="tile v16" role="img" aria-label="Music video still: backyard party with balloons"><svg class="play" width="40" height="40"><use href="#play"/></svg></li>
  </ul>

  <a class="btn-more">See more videos <svg width="10" height="10"><use href="#arrow"/></svg></a>
  <div class="divider"></div>

  <footer>
    <div class="logo footer-logo">Oliver Trask</div>
    <div class="contact">
      <svg width="24" height="24"><use href="#mail"/></svg>
      <span>olivertraskmgmt@mailbox.com</span>
    </div>
    <ul class="social"><li>Linkwell</li><li>Framehouse</li></ul>
    <p class="footer-nav">Direction<span>/</span>Executive Production<br>Commissioned<span>/</span>Contact</p>
    <p class="legal">© 2020 Oliver Trask . All Rights reserved<br>Privacy &nbsp;|&nbsp; Terms and use</p>
  </footer>
</section>

</body>
</html>
```